Brightvale Landscape & Construction Website

I have created a detailed txt document and included it in the files upload that will provide all the project details because trying to list it in here is cumbersome. This is for a website only. I have my own team to handle the psd to html conversion. They have an existing website which I have added in the doc. I have also upload various logo files to be used.

Industry/Entity Type

Landscape and Construction

Number of Pages Required

1 page

```html
<!DOCTYPE html>
<html lang="en">
<head>
<meta charset="utf-8">
<title>Brightvale Landscape &amp; Construction</title>
<link rel="stylesheet" href="https://fonts.googleapis.com/css2?family=Anton&family=Inter:wght@400;500;600;700&display=swap">
<style>
:root{
  --orange:#ee6a24;
  --red:#e8412b;
  --dark:#222222;
  --gallery:#262626;
  --text:#4a4a4a;
  --muted:#8a8a8a;
  --light:#f4f5f7;
  --line:#d9dbe0;
  --tint:#fbe3d6;
}
*{box-sizing:border-box;margin:0;padding:0}
html,body{width:1200px;height:3359px;overflow:hidden}
body{font-family:"Inter",Arial,sans-serif;color:var(--text);background:#fff;position:relative}
.abs{position:absolute}
.display{font-family:"Anton",Impact,sans-serif;font-weight:400;letter-spacing:.3px}

/* top bar */
.topbar{top:0;left:0;width:1200px;height:29px;background:var(--dark)}
.topbar .social{top:0;left:0;width:248px;height:29px;background:#fff;clip-path:polygon(0 0,215px 0,248px 29px,0 29px)}
.social span{position:absolute;top:7px;width:14px;height:14px;border-radius:50%;background:var(--dark)}
.topbar .addr{right:44px;top:8px;font-size:10px;color:#cfcfcf}

/* header */
.brand{left:44px;top:40px;display:flex;align-items:center;gap:8px}
.brand i{width:28px;height:28px;border-radius:50%;background:var(--orange);display:block}
.brand b{font-size:19px;font-weight:700;color:var(--orange);letter-spacing:.2px}
.contact{display:flex;align-items:center;gap:9px;top:43px}
.contact .ic{width:26px;height:26px;border-radius:50%;background:var(--orange);display:flex;align-items:center;justify-content:center}
.contact strong{display:block;font-size:12px;color:var(--dark);font-weight:600}
.contact small{display:block;font-size:9px;color:var(--muted)}
.quote{left:1055px;top:42px;width:101px;height:30px;background:var(--orange);color:#fff;font-size:11px;font-weight:500;display:flex;align-items:center;justify-content:center;border-radius:2px}

/* nav */
.nav{left:44px;top:89px;width:1112px;height:41px;background:var(--red);border-radius:4px;z-index:3;display:flex;justify-content:center;gap:28px;align-items:center;padding-right:14px}
.nav a{color:#fff;font-size:12.5px;text-decoration:none;position:relative;height:41px;line-height:41px}
.nav a.active{font-weight:700}
.nav a.active::after{content:"";position:absolute;left:0;right:0;bottom:0;height:3px;background:#fff}

/* hero */
.hero{left:0;top:110px;width:1200px;height:594px;background:linear-gradient(100deg,#3c3a35 0%,#5d5a52 45%,#78766f 70%,#4a4840 100%)}
.hero::after{content:"";position:absolute;inset:0;background:rgba(0,0,0,.28)}
.hero-copy{left:124px;top:160px;z-index:2;color:#fff}
.hero-copy h1{font-size:60px;line-height:62px}
.hero-copy p{margin-top:32px;font-size:27px;line-height:37px;width:720px;font-weight:400}
.arrow{top:300px;z-index:2}
.dots{left:571px;top:551px;display:flex;gap:6px;z-index:2}
.dots span{width:10px;height:10px;border-radius:50%;background:rgba(255,255,255,.45)}
.dots span:first-child{background:var(--orange)}

/* service panels */
.panel{top:704px;width:600px;height:394px;color:#fff;text-align:center}
.panel.land{left:0;background:linear-gradient(160deg,#b57a22,#a3661a)}
.panel.build{left:600px;background:linear-gradient(160deg,#b8522e,#a2412a)}
.panel .badge{position:absolute;left:269px;top:48px;width:62px;height:62px;border:2px solid #fff;border-radius:50%;display:flex;align-items:center;justify-content:center}
.panel h2{position:absolute;left:0;right:0;top:130px;font-size:42px;line-height:50px}
.panel .bar{position:absolute;left:268px;top:188px;width:64px;height:4px;background:#fff}
.panel p{position:absolute;left:70px;right:70px;top:210px;font-size:16px;line-height:25px}
.panel .btn{position:absolute;left:237px;top:308px;width:127px;height:35px;border:1px solid #fff;border-radius:2px;font-size:12px;line-height:33px;font-weight:500}

/* about */
.eyebrow{font-size:12px;color:var(--dark);font-weight:500;letter-spacing:.2px}
.title{font-size:40px;line-height:48px;color:var(--dark)}
.underline{height:4px;background:var(--orange)}
.about-text p{font-size:16px;line-height:24.5px;color:var(--text);margin-bottom:25px}
.photo{background:linear-gradient(135deg,#5a7da8,#8a98a8 55%,#6b5a44)}

/* service area */
.services{left:0;top:1558px;width:1200px;height:760px;background:var(--light)}
.card{background:#f4f5f7;border:1px solid var(--line);width:221px;height:175px}
.card .num{position:absolute;left:20px;top:22px;font-size:10px;color:var(--muted);font-weight:600}
.card svg{position:absolute;left:20px;top:56px}
.card h3{position:absolute;left:20px;top:114px;font-size:16px;font-weight:600;color:var(--dark)}
.card .more{position:absolute;left:20px;top:141px;font-size:10px;color:#555;font-weight:500;letter-spacing:.2px}
.card .more em{color:var(--orange);font-style:normal;margin-left:4px}
.btn-outline{border:1px solid var(--orange);font-size:12px;color:var(--dark);display:flex;align-items:center;justify-content:center;border-radius:2px;background:transparent}

/* gallery */
.gallery{left:0;top:2282px;width:1200px;height:747px}
.gallery .shot{position:absolute;width:300px;height:225px}

/* footer */
.footer{left:0;top:3029px;width:1200px;height:330px;background:#f6f6f6;border-top:3px solid var(--orange)}
.footer h4{position:absolute;top:52px;font-size:16px;font-weight:600;color:var(--dark)}
.footer ul{position:absolute;top:86px;list-style:none}
.footer li{font-size:12px;color:#777;height:28.5px}
.footer .addr-lines{position:absolute;left:888px;top:87px;font-size:12px;line-height:17.6px;color:#777}
.footer .addr-lines a{color:var(--orange);text-decoration:none}
.footer .about{position:absolute;left:134px;top:90px;width:295px;font-size:10px;line-height:15.6px;color:#888}
.footer .copy{position:absolute;left:0;right:0;top:274px;text-align:center;font-size:11px;color:#888}
</style>
</head>
<body>

<!-- top bar -->
<div class="abs topbar">
  <div class="abs social">
    <span style="left:43px"></span><span style="left:68px"></span><span style="left:92px"></span><span style="left:117px"></span><span style="left:142px"></span>
  </div>
  <div class="abs addr">1840 Ridgeview Ave NE Cedar Falls, MN 55000</div>
</div>

<!-- header -->
<div class="abs brand"><i></i><b>Brightvale</b></div>
<div class="abs contact" style="left:661px">
  <div class="ic"><svg width="13" height="13" viewBox="0 0 24 24" fill="none" stroke="#fff" stroke-width="2"><path d="M5 3h4l2 5-3 2a11 11 0 0 0 6 6l2-3 5 2v4a2 2 0 0 1-2 2A17 17 0 0 1 3 5a2 2 0 0 1 2-2z"/></svg></div>
  <div><strong>555.201.4580</strong><small>Call Now !</small></div>
</div>
<div class="abs contact" style="left:810px">
  <div class="ic"><svg width="13" height="13" viewBox="0 0 24 24" fill="none" stroke="#fff" stroke-width="2"><rect x="3" y="5" width="18" height="14" rx="1"/><path d="M3 6l9 7 9-7"/></svg></div>
  <div><strong>info@brightvalelandscape.com</strong><small>Email Now !</small></div>
</div>
<div class="abs quote">Get a Quote</div>

<!-- navigation -->
<nav class="abs nav">
  <a class="active">Home</a><a>Landscape Services</a><a>Construction Services</a><a>Company</a><a>Contact</a><a>FAQs</a><a>Gallery</a>
</nav>

<!-- hero -->
<section class="abs hero" role="img" aria-label="Photo of a house exterior with a white lattice screen and siding">
  <div class="abs hero-copy">
    <h1 class="display">Safe, Reliable &amp;<br>High Quality Construction</h1>
    <p>We are a long-established full service residential and commercial licensed construction company and landscape/hardscape installer.</p>
  </div>
  <svg class="abs arrow" style="left:40px" width="24" height="40" viewBox="0 0 24 40"><path d="M20 4 4 20l16 16" fill="none" stroke="#fff" stroke-width="3"/></svg>
  <svg class="abs arrow" style="left:1136px" width="24" height="40" viewBox="0 0 24 40"><path d="M4 4l16 16L4 36" fill="none" stroke="#fff" stroke-width="3"/></svg>
  <div class="abs dots"><span></span><span></span><span></span><span></span></div>
</section>

<!-- service panels -->
<section class="abs panel land" role="img" aria-label="Landscaped yard with boulders, tinted amber">
  <div class="badge"><svg width="30" height="30" viewBox="0 0 24 24" fill="none" stroke="#fff" stroke-width="1.6"><path d="M7 11v9H3v-9zM7 11l4-8a2 2 0 0 1 3 2l-1 5h6a2 2 0 0 1 2 2l-2 7a2 2 0 0 1-2 1H7"/></svg></div>
  <h2 class="display">Landscape Services</h2>
  <div class="bar"></div>
  <p>Landscaping we offer design, pavers, retaining walls, and everything in between. We provide our own trucking, excavating and grading work.</p>
  <div class="btn">Find Out More</div>
</section>
<section class="abs panel build" role="img" aria-label="Wooden deck with railings, tinted red">
  <div class="badge"><svg width="30" height="30" viewBox="0 0 24 24" fill="none" stroke="#fff" stroke-width="1.6"><path d="M7 11v9H3v-9zM7 11l4-8a2 2 0 0 1 3 2l-1 5h6a2 2 0 0 1 2 2l-2 7a2 2 0 0 1-2 1H7"/></svg></div>
  <h2 class="display">Construction Services</h2>
  <div class="bar"></div>
  <p>Our construction consists of custom decks, screen rooms, three- and four-season additions, remodels, foundation repair, roofing and siding, soffits, gutters, windows and doors.</p>
  <div class="btn">Find Out More</div>
</section>

<!-- about -->
<section class="about">
  <div class="abs eyebrow" style="left:132px;top:1142px">ABOUT US</div>
  <h2 class="abs title display" style="left:132px;top:1164px">Welcome</h2>
  <div class="abs underline" style="left:132px;top:1221px;width:78px"></div>
  <div class="abs about-text" style="left:132px;top:1244px;width:535px">
    <p>Our construction consists of custom decks, screen rooms, three- and four-season additions, remodels, foundation repair, roofing and siding, soffits, gutters, windows and doors.</p>
    <p>We also build pole barns, garages and cabins. Landscaping we offer design, pavers, retaining walls, and everything in between. We provide our own trucking, excavating and grading work. If you are looking for interior work, we are able to remodel any room in your house.</p>
  </div>
  <div class="abs" style="left:824px;top:1142px;width:240px;height:162px;background:var(--tint);opacity:.6" role="img" aria-label="Decorative square grid"></div>
  <div class="abs photo" style="left:699px;top:1205px;width:302px;height:193px" role="img" aria-label="Worker framing a wooden structure against blue sky"></div>
  <div class="abs photo" style="left:794px;top:1333px;width:273px;height:180px;background:linear-gradient(135deg,#a8a49c,#d9d4cb 50%,#8c8478)" role="img" aria-label="Smiling construction worker in a hard hat"></div>
</section>

<!-- service area -->
<section class="abs services">
  <div class="abs" style="left:23px;top:36px;width:153px;height:151px;background:var(--tint);opacity:.7;clip-path:polygon(0 0,100% 0,100% 28%,57% 28%,57% 57%,28% 57%,28% 100%,0 100%)" role="img" aria-label="Decorative square grid"></div>
  <div class="abs eyebrow" style="right:498px;top:44px;font-size:11px">WHAT WE OFFER</div>
  <h2 class="abs title display" style="right:498px;top:70px;font-size:38px">Service Area</h2>
  <div class="abs underline" style="left:623px;top:125px;width:79px"></div>
  <p class="abs" style="right:498px;top:148px;width:520px;text-align:right;font-size:15.5px;line-height:24.5px">We have a wealth of experience working as main building contractors on all kinds of projects, big and small, from home maintenance and improvements to extensions, refurbishments and new builds.</p>
  <div class="abs btn-outline" style="left:575px;top:245px;width:127px;height:36px">Find Out More</div>
</section>

<div class="abs card" style="left:765px;top:1603px;width:302px;height:258px">
  <span class="num" style="top:38px">01.</span>
  <svg style="top:90px" width="48" height="48" viewBox="0 0 48 48" fill="none" stroke="var(--orange)" stroke-width="2"><path d="M6 34h10v-8h14V12M24 12h12M36 8v8M12 30a4 4 0 1 0 0 8M30 6h12"/><circle cx="12" cy="40" r="3"/></svg>
  <h3 style="top:190px">Water Features/Outdoor Fire Pits</h3>
  <span class="more" style="top:216px">VIEW MORE<em>↗</em></span>
</div>

<div class="abs card" style="left:132px;top:1878px">
  <span class="num">01.</span>
  <svg width="46" height="46" viewBox="0 0 46 46" fill="none" stroke="var(--orange)" stroke-width="2"><rect x="4" y="18" width="38" height="22"/><path d="M4 29h38M17 18v11M30 18v11M11 29v11M24 29v11M36 29v11M10 18V8h14v10"/></svg>
  <h3>Pavers</h3><span class="more">VIEW MORE<em>↗</em></span>
</div>
<div class="abs card" style="left:370px;top:1878px">
  <span class="num">01.</span>
  <svg width="46" height="46" viewBox="0 0 46 46" fill="none" stroke="var(--orange)" stroke-width="2"><ellipse cx="16" cy="36" rx="11" ry="6"/><ellipse cx="30" cy="24" rx="10" ry="6"/><ellipse cx="18" cy="13" rx="8" ry="5"/></svg>
  <h3>Boulder/Retaining Walls</h3><span class="more">VIEW MORE<em>↗</em></span>
</div>
<div class="abs card" style="left:608px;top:1878px">
  <span class="num">01.</span>
  <svg width="46" height="46" viewBox="0 0 46 46" fill="none" stroke="var(--orange)" stroke-width="2"><path d="M8 42V20M8 20c-6-6 0-14 0-14s6 8 0 14M22 42V14M22 14c-6-6 0-12 0-12s6 6 0 12M4 42h38M30 24h12v18H30z"/></svg>
  <h3>General Landscaping</h3><span class="more">VIEW MORE<em>↗</em></span>
</div>
<div class="abs card" style="left:846px;top:1878px">
  <span class="num">01.</span>
  <svg width="46" height="46" viewBox="0 0 46 46" fill="none" stroke="var(--orange)" stroke-width="2"><path d="M4 30 30 4l12 12-26 26zM10 24l12 12M17 17l12 12M24 10l12 12"/></svg>
  <h3>Decks/Additions</h3><span class="more">VIEW MORE<em>↗</em></span>
</div>
<div class="abs card" style="left:132px;top:2070px">
  <span class="num">01.</span>
  <svg width="46" height="46" viewBox="0 0 46 46" fill="none" stroke="var(--orange)" stroke-width="2"><path d="M4 22 23 5l19 17M9 18v24h28V18M19 42V30h8v12"/></svg>
  <h3>Remodels</h3><span class="more">VIEW MORE<em>↗</em></span>
</div>
<div class="abs card" style="left:370px;top:2070px">
  <span class="num">01.</span>
  <svg width="46" height="46" viewBox="0 0 46 46" fill="none" stroke="var(--orange)" stroke-width="2"><path d="M6 20 23 6l17 14v22H6zM14 42V26h18v16M14 26l18 16M32 26 14 42"/></svg>
  <h3>Pole Barns</h3><span class="more">VIEW MORE<em>↗</em></span>
</div>
<div class="abs card" style="left:608px;top:2070px">
  <span class="num">01.</span>
  <svg width="46" height="46" viewBox="0 0 46 46" fill="none" stroke="var(--orange)" stroke-width="2"><rect x="4" y="26" width="24" height="10"/><path d="M10 26v-8h10v8M28 30l8-18 6 4-4 10"/><circle cx="10" cy="40" r="3"/><circle cx="22" cy="40" r="3"/></svg>
  <h3>Bobcat Work</h3><span class="more">VIEW MORE<em>↗</em></span>
</div>
<div class="abs card" style="left:846px;top:2070px">
  <span class="num">01.</span>
  <svg width="46" height="46" viewBox="0 0 46 46" fill="none" stroke="var(--orange)" stroke-width="2"><path d="M23 8 42 40H4z"/><path d="M8 14l12 12M20 14 8 26"/><circle cx="26" cy="32" r="4"/></svg>
  <h3>Miscellaneous</h3><span class="more">VIEW MORE<em>↗</em></span>
</div>

<!-- gallery -->
<section class="abs gallery">
  <svg class="abs" style="left:0;top:0" width="1200" height="120" viewBox="0 0 1200 120" preserveAspectRatio="none">
    <polygon points="0,100 600,2 1200,100 1200,120 0,120" fill="var(--orange)"/>
    <polygon points="0,116 600,6 1200,116 1200,120 0,120" fill="var(--gallery)"/>
  </svg>
  <div class="abs" style="left:0;top:119px;width:1200px;height:178px;background:var(--gallery)"></div>
  <div class="abs" style="left:0;top:88px;width:1200px;text-align:center;color:#fff">
    <h2 class="display" style="font-size:40px;line-height:50px">Project Gallery</h2>
  </div>
  <div class="abs underline" style="left:557px;top:144px;width:86px"></div>
  <p class="abs" style="left:0;width:1200px;top:170px;text-align:center;color:#fff;font-size:15px">Top Quality With Personal Attention To Your Needs explore All Our Projects</p>
  <div class="abs btn-outline" style="left:545px;top:219px;width:110px;height:34px;color:#fff;font-size:11.5px">All Projects</div>
  <div class="abs" style="left:978px;top:222px;width:154px;height:75px;background:#3a3a3a;clip-path:polygon(40% 0,100% 0,100% 100%,0 100%,0 50%,40% 50%)" role="img" aria-label="Decorative square grid"></div>
  <div class="shot" style="left:0;top:297px;background:linear-gradient(160deg,#b9ab94,#7a5a3c)" role="img" aria-label="Wooden deck stairs beside a house"></div>
  <div class="shot" style="left:300px;top:297px;background:linear-gradient(160deg,#6a6f74,#5f7f3e 60%,#9a9690)" role="img" aria-label="Stone paver walkway beside shrubs"></div>
  <div class="shot" style="left:600px;top:297px;background:linear-gradient(160deg,#6b3f22,#a0653a 55%,#d8d0c4)" role="img" aria-label="Interior wooden staircase"></div>
  <div class="shot" style="left:900px;top:297px;background:linear-gradient(160deg,#a7aeb0,#6a7f4a 60%,#8f8a80)" role="img" aria-label="Garden beds with flowers"></div>
  <div class="shot" style="left:0;top:522px;background:linear-gradient(160deg,#d0d4d6,#5d8a3a 60%,#8a6a4c)" role="img" aria-label="Landscaped front yard with rock border"></div>
  <div class="shot" style="left:300px;top:522px;background:linear-gradient(160deg,#8a8e92,#4a3a30 60%,#6f7a4a)" role="img" aria-label="Elevated deck with dark railing"></div>
  <div class="shot" style="left:600px;top:522px;background:linear-gradient(160deg,#8a7a66,#9a6650 60%,#6f6a6a)" role="img" aria-label="Brick paver patio"></div>
  <div class="shot" style="left:900px;top:522px;background:linear-gradient(160deg,#b69a76,#5f8a3e 55%,#7a5a40)" role="img" aria-label="Mulch garden bed along a house wall"></div>
</section>

<!-- footer -->
<footer class="abs footer">
  <h4 style="left:134px">Contact Us</h4>
  <p class="about">Daniel Marsh, President and Owner of Brightvale Landscape &amp; Construction Inc., began mowing lawns and plowing snow at sixteen for local homes and businesses. While studying building trades at a technical college, he kept his focus on his own lawn and landscape business.</p>
  <div class="abs" style="left:134px;top:271px;display:flex;align-items:center;gap:6px">
    <i style="display:block;width:20px;height:20px;border-radius:50%;background:var(--orange)"></i>
    <b style="font-size:15px;font-weight:700;color:var(--dark)">Brightvale</b>
  </div>
  <h4 style="left:514px">Navigation Menu</h4>
  <ul style="left:514px"><li>Landscape Services</li><li>Construction Services</li><li>Company</li><li>FAQs</li><li>Gallery</li></ul>
  <h4 style="left:720px">Other</h4>
  <ul style="left:720px"><li>Privacy Policy</li><li>Terms Condition</li><li style="height:38px">FAQ</li><li>Contact Us</li></ul>
  <h4 style="left:888px">Contact Us</h4>
  <div class="addr-lines">1840 Ridgeview Ave NE<br>Cedar Falls, MN&nbsp; 55000<br>Phone 555.201.4580<br>Fax 555.201.4581<br><a>info@brightvalelandscape.com</a></div>
  <div class="copy">Copyright © 2022 Brightvale Landscape &amp; Construction Inc. All Rights Reserved</div>
</footer>

</body>
</html>
```